Revolutionary Video Platform (uncoded) - updated 05.11.

We want you to design the frontpage (uncoded) of FLIRTNOVA.net (we ev. hire the winner to create the subpages).

The concept of FLIRTNOVA.net is to show (ONLY!) infield videos of dating coaches (when they get in contact with women on the street) so that the users will have a solid base for deciding which coach they want to contact. I highlight that because some designs contained other ideas like "dating tips". No, we are specialized on infield videos. People should see if these coaches are really worth their money.

Therefore, the frontpage must include the following:

Header: Logo (attached), writing "FLIRTNOVA" or "FLIRT NOVA", links "Contact", "About", "Sign In", "Sign Up"

No design yet tried to change the logo in its size. You're welcome to do creative stuff.

What else is necessary on the front page:

1. 2 statements:

"Because 34 videos prove how to get every woman you want."
"Connect directly with 26 dating-coaches from these videos!"

The numbers should be showed in a way that the users know that they count up automatically; important: use the style zemlo has on it's front page by showing their amount of users.

2. Top rated Dating Coaches:

As the videos on the site can be rated, we want the coaches with the best rated videos on the front page with their faces (people can jump from there directly to their profiles).

To the pictures of the coaches you should also add the country flag and the city (where they come from). Plus, users should see who's on the first place, who's on the second place.. max. 10 coaches on the front page..

Set the title "TOP 10 DATING COACHES listed by best rated videos"

3. Search System

In order to find the videos the user is searching for, it needs a simple search form, where they can search after:

- Language
- Country
- City
- Rating
- Level of Difficulty
- Set-Size
- Conversation Starter

You can use simple white bars with a drop-down button.

4. Tags

Implement tags like "bitch shield, blow out opener, bounce, calibration, canned routine, challenge point, cockblock, cold approach, cold reading, compliment opener" etc.

Alphabetically listed..

5. Create previews of the (searched) videos which contains:

- Thumbnail of the video (only thumbnails on front page, no bigger video playback window, pls use pictures in order to make the site look more real)

- Some infos about the video (name of the coach with user-picture, duration, language, country (name and flag), city, audio comment (yes/no), difficulty level (super easy-expert), views, points needed to view (1-3), 5 star rating)

- Title and the beginning of the text about the video (written by the coach), i.e. about 30 words

- There are 2 sorts of videos.. (it's not necessary to explain why, it's just important that you implement two different versions of the video preview area (different only in terms of color!).. for example, some video preview areas could be edged in gold, others in silver.. or you could fill the whole video preview area with a color.. show me your taste... even though I prefer the more elegant way like gold and silver, you can probably surprise me with other color combinations..

- In order to simplify the process of comparing your designs, pls create 4 such preview video are areas..

6. Best voted video reviewer:

Users AND coaches will be able to write reviews about the videos. These reviews can be liked/voted. Therefore, we will know which user or coach writes the best reviews.

So we want you to implement also the charts of the 10 best voted video reviewers. Make sure there is a ranking list with the name of the user/coach and how many likes he got.
Here as well: add country flag, country and city (to see where they come from)..plus a little thumbnail of the profile picture.. Make sure the best 3 are being highlighted somehow..
Updates

Some designs were quite creative so far.
But unfortunately, less than half of the designers considered all requirements.
Therefore, be sure to implement all the requirements (for example, check new point nr. 6).
Without considering all the requirements, you don't have a chance to win this content.

Thank you.

Target Market(s)

male, 16-40 years old, worldwide audience

Industry/Entity Type

Dating

Requirements
Must have
• Not all submitted designs considered all requirements.

Therefore, please read the requirements carefully and consider all of them. If you want to add some new ideas or if you decide not to implement some requirements, I suggest to submit a second design.
Nice to have
• - if you have other ideas, feel free to add some of them to the front page, probably in form of a second design

- sometimes the same page will look totally different in other colors. Therefore, it would be great to add a 2nd version of your design, in terms of color

- the front page needs to be an eye-catcher

- different FLIRTNOVA font styles (come up with your own taste), a few different styles would be great!
Should not have
• - a search field like there is one in the first submitted design (the intelligent search is already being available with the filter system and the tags)

- female colors like pink/purple (it's a site only for men)

- a 08/15 look.. this will be the first website worldwide which contains videos from the best dating gurus on this planet in action.. they deserve a cool place to show their videos in order to gain new customers..

```html
<!DOCTYPE html>
<html lang="en">
<head>
<meta charset="utf-8">
<title>FlirtNova – Infield Dating Videos</title>
<link rel="stylesheet" href="https://fonts.googleapis.com/css2?family=Ubuntu:wght@400;500;700&family=Noto+Serif:wght@400&family=Noto+Sans:wght@400;700&display=swap">
<style>
  :root{
    --header-top:#4f86bb;
    --header-bottom:#2d5595;
    --page-bg:#e3ecf3;
    --panel-bg:#f3f6f9;
    --panel-edge:#9fc7df;
    --navy:#2d4f8c;
    --navy-dark:#223f73;
    --gold:#f4c21a;
    --white:#ffffff;
    --text-dark:#333333;
    --muted:#8a8a8a;
    --grey-select:#bdbdbd;
    --star:#f2c313;
    --star-off:#c9c9c9;
  }
  *{box-sizing:border-box;margin:0;padding:0}
  html,body{width:1200px;height:1000px;overflow:hidden}
  body{position:relative;background:var(--page-bg);font-family:"Ubuntu",sans-serif;color:var(--text-dark)}
  .abs{position:absolute}

  /* Header */
  .site-header{position:absolute;left:0;top:0;width:1200px;height:336px;
    background:radial-gradient(ellipse at 20% 0%,#5e98c9 0%,transparent 55%),linear-gradient(180deg,var(--header-top),var(--header-bottom) 80%)}
  .zigzag{position:absolute;left:0;top:322px}
  .account{position:absolute;left:762px;top:14px;width:308px;height:40px;border-bottom:1px dashed #9ab8db}
  .account-label{position:absolute;left:0;top:4px;color:var(--white);font-size:14px}
  .account-input{position:absolute;top:0;height:24px;background:#3d6aa6;border:1px solid #5480b8;color:#d5e2f2;font-size:11px;padding:4px 8px}
  .account-go{position:absolute;left:283px;top:0;width:25px;height:24px;background:#5c8cc4;color:#e6eefa;font-size:10px;text-align:center;line-height:24px}

  .brand{position:absolute;left:130px;top:140px;color:var(--white);font-weight:700;font-size:37px;letter-spacing:-.5px}
  .brand-mark{position:absolute;left:205px;top:48px;width:62px;height:62px;border-radius:50%;background:var(--white)}
  .brand-tag{position:absolute;left:358px;top:161px;color:#cfe0f1;font-size:14px;font-weight:500}
  .brand-tag b{font-weight:500;margin-right:12px;color:var(--white)}

  .main-nav{position:absolute;top:159px;right:130px;display:flex;gap:24px}
  .main-nav a{color:var(--gold);text-decoration:none;font-weight:500;font-size:16px}

  .counter{position:absolute;left:130px;display:flex;align-items:center}
  .counter .digit{width:20px;height:31px;margin-right:3px;background:linear-gradient(#ffffff 50%,#e4e9ef 50%);border-radius:2px;color:#3a5d95;font-size:17px;text-align:center;line-height:31px;box-shadow:0 1px 2px rgba(0,0,0,.3)}
  .counter .statement{margin-left:12px;color:#dbe8f5;font-size:14px;font-weight:500}

  /* Filter */
  .filter-tab{position:absolute;left:130px;top:369px;width:187px;height:70px;background:var(--panel-bg);border-radius:4px 4px 0 0}
  .filter-tab span{position:absolute;left:90px;top:27px;font-weight:700;font-size:15px}
  .filter-tab svg{position:absolute;left:40px;top:20px}
  .tab-button{position:absolute;top:369px;height:49px;background:linear-gradient(#3c6bab,#2b5594);border-radius:4px;color:var(--gold);font-weight:700;font-size:14px;text-align:center;line-height:49px;box-shadow:0 2px 3px rgba(0,0,0,.25)}
  .tab-button::before{content:"";position:absolute;inset:4px;border:1px dashed #7fa3d2;border-radius:3px}
  .filter-panel{position:absolute;left:130px;top:436px;width:940px;height:278px;background:var(--panel-bg);border-bottom:3px solid var(--panel-edge);border-radius:0 4px 4px 4px}
  .field-label{position:absolute;color:var(--navy);font-weight:500;font-size:15px;line-height:18px}
  .select{position:absolute;width:260px;height:38px;border-radius:3px;font-size:13px;line-height:38px;padding-left:15px}
  .select svg{position:absolute;right:12px;top:11px}
  .select.active{background:linear-gradient(#4571b0,#2d5594);color:var(--white);border:1px solid #27497f}
  .select.empty{background:linear-gradient(#cfcfcf,#b5b5b5);color:#f4f4f4;border:1px solid #aaa}
  .slider-scale{position:absolute;font-family:"Noto Serif",serif;font-size:12px;color:var(--navy)}
  .tip{position:absolute;left:25px;top:227px;display:flex;align-items:center;font-family:"Noto Serif",serif;font-size:14px}
  .tip i{width:35px;height:35px;border-radius:50%;background:#333;color:#fff;font-style:normal;font-weight:700;font-size:18px;text-align:center;line-height:35px;margin-right:11px;font-family:"Noto Serif",serif}
  .panel-go{position:absolute;left:885px;top:227px;width:42px;height:40px;background:var(--navy);border-radius:4px;color:var(--gold);font-weight:700;font-size:14px;text-align:center;line-height:40px}

  /* Video previews */
  .video-list{position:absolute;left:130px;top:746px;width:940px;height:270px;background:var(--white);border-radius:4px}
  .video-list::after{content:"";position:absolute;left:470px;top:10px;bottom:0;border-left:1px dashed #dde3ea}
  .video-card{position:absolute;top:0;width:470px;height:260px;font-family:"Noto Sans",sans-serif}
  .coach-avatar{position:absolute;left:25px;top:21px;width:41px;height:41px;border:1px solid #d6d6d6;background:#fff}
  .coach-name{position:absolute;left:83px;top:34px;font-size:13px;color:var(--navy-dark)}
  .points{position:absolute;right:36px;top:34px;font-size:13px;color:var(--navy);text-decoration:underline}
  .thumb{position:absolute;left:27px;top:88px;width:186px;height:156px;background:#000}
  .video-title{position:absolute;left:228px;top:86px;font-size:13px;font-weight:700;color:var(--navy-dark);white-space:nowrap}
  .meta{position:absolute;left:228px;top:110px;font-size:11px;line-height:14px;color:var(--muted)}
  .meta.right{left:325px}
  .meta .views{color:var(--navy)}
  .stars{position:absolute;left:228px;top:157px;display:flex;gap:5px}
  .audio{position:absolute;left:229px;top:182px;font-size:12px;color:#111;text-decoration:underline;display:flex;align-items:center}
  .audio svg{margin-left:9px}
  .excerpt{position:absolute;left:229px;top:202px;width:225px;font-size:12px;line-height:14px;color:#111}
</style>
</head>
<body>

<header class="site-header">
  <div class="account">
    <span class="account-label">Account</span>
    <div class="account-input" style="left:64px;width:106px">login</div>
    <div class="account-input" style="left:174px;width:106px">password</div>
    <div class="account-go">GO</div>
  </div>

  <div class="brand-mark"></div>
  <div class="brand">FlirtNova</div>
  <div class="brand-tag"><b>,</b>because</div>

  <nav class="main-nav">
    <a href="#">Contact</a><a href="#">About</a><a href="#">Follow</a><a href="#">Sign In</a><a href="#">Sign Up</a>
  </nav>

  <div class="counter" style="top:214px">
    <span class="digit">1</span><span class="digit">2</span><span class="digit">8</span>
    <span class="statement">Videos show how to get every woman you want.</span>
  </div>
  <div class="counter" style="top:252px">
    <span class="digit">3</span><span class="digit">7</span><span class="digit">1</span><span class="digit">1</span><span class="digit">2</span><span class="digit">1</span>
    <span class="statement">Connect directly with 26 dating-coaches worldwide!</span>
  </div>

  <svg class="zigzag" width="1200" height="14" viewBox="0 0 1200 14">
    <defs>
      <pattern id="teeth" width="10" height="14" patternUnits="userSpaceOnUse">
        <path d="M0 14 L5 4 L10 14 Z" fill="#e3ecf3"/>
      </pattern>
    </defs>
    <rect width="1200" height="14" fill="url(#teeth)"/>
  </svg>
</header>

<div class="filter-tab">
  <svg width="24" height="30" viewBox="0 0 24 30"><path d="M1 2 Q12 -1 23 2 L14 14 L12 28 L10 14 Z" fill="#7ec3e0"/></svg>
  <span>Filter</span>
</div>
<div class="tab-button" style="left:760px;width:145px">Recently added</div>
<div class="tab-button" style="left:922px;width:146px">10 best rated</div>

<section class="filter-panel">
  <div class="field-label" style="left:24px;top:24px">Language</div>
  <div class="select active" style="left:148px;top:17px">Polish, English, Spanish<svg width="10" height="17"><path d="M5 0 L10 7 H0Z M0 10 H10 L5 17Z" fill="#fff"/></svg></div>
  <div class="field-label" style="left:24px;top:75px">Country</div>
  <div class="select active" style="left:148px;top:67px">USA, Poland<svg width="10" height="17"><path d="M5 0 L10 7 H0Z M0 10 H10 L5 17Z" fill="#fff"/></svg></div>
  <div class="field-label" style="left:24px;top:126px">City</div>
  <div class="select empty" style="left:148px;top:117px">Undefined<svg width="10" height="17"><path d="M5 0 L10 7 H0Z M0 10 H10 L5 17Z" fill="#fff"/></svg></div>
  <div class="field-label" style="left:24px;top:168px">Conversation<br>Starter</div>
  <div class="select empty" style="left:148px;top:167px">Undefined<svg width="10" height="17"><path d="M5 0 L10 7 H0Z M0 10 H10 L5 17Z" fill="#fff"/></svg></div>

  <div class="field-label" style="left:479px;top:24px">Rating</div>
  <span class="slider-scale" style="left:659px;top:13px">1</span>
  <span class="slider-scale" style="left:713px;top:13px">2</span>
  <span class="slider-scale" style="left:767px;top:13px">3</span>
  <span class="slider-scale" style="left:821px;top:13px">4</span>
  <span class="slider-scale" style="left:876px;top:13px">5</span>
  <svg class="abs" style="left:654px;top:28px" width="232" height="22">
    <rect x="2" y="8" width="228" height="5" rx="2" fill="#dde4ea"/>
    <rect x="62" y="8" width="163" height="5" fill="#2d4f8c"/>
    <circle cx="62" cy="11" r="8" fill="#fff" stroke="#2d4f8c" stroke-width="3"/>
    <circle cx="225" cy="11" r="8" fill="#fff" stroke="#2d4f8c" stroke-width="3"/>
  </svg>

  <div class="field-label" style="left:479px;top:75px">Level of Difficulty</div>
  <span class="slider-scale" style="left:650px;top:61px">Easy</span>
  <span class="slider-scale" style="left:748px;top:61px">Medium</span>
  <span class="slider-scale" style="left:865px;top:61px">Hard</span>
  <svg class="abs" style="left:654px;top:77px" width="232" height="22">
    <rect x="2" y="7" width="228" height="5" rx="2" fill="#dde4ea"/>
    <circle cx="117" cy="11" r="8" fill="#fff" stroke="#2d4f8c" stroke-width="3"/>
  </svg>

  <div class="field-label" style="left:479px;top:126px">Set-Size</div>
  <div class="select empty" style="left:644px;top:117px">Undefined<svg width="10" height="17"><path d="M5 0 L10 7 H0Z M0 10 H10 L5 17Z" fill="#fff"/></svg></div>

  <div class="tip"><i>i</i>Tip: You can select more positions holding CTRL.</div>
  <div class="panel-go">GO</div>
</section>

<section class="video-list">
  <article class="video-card" style="left:0">
    <div class="coach-avatar"></div>
    <div class="coach-name">Commodo Egestas</div>
    <a class="points">need 360 points</a>
    <div class="thumb" role="img" aria-label="Video thumbnail of an infield approach"></div>
    <h3 class="video-title">Duis consectetur, velit et tincidunt.</h3>
    <div class="meta"><span class="views">26 110 views</span><br>Difficulty: hard<br>5:13</div>
    <div class="meta right">English<br>USA<br>New York</div>
    <div class="stars">
      <svg width="19" height="18" viewBox="0 0 20 19"><path d="M10 0l3 6.5 7 .8-5.2 4.8 1.4 6.9L10 15.5 3.8 19l1.4-6.9L0 7.3l7-.8z" fill="#f2c313"/></svg>
      <svg width="19" height="18" viewBox="0 0 20 19"><path d="M10 0l3 6.5 7 .8-5.2 4.8 1.4 6.9L10 15.5 3.8 19l1.4-6.9L0 7.3l7-.8z" fill="#f2c313"/></svg>
      <svg width="19" height="18" viewBox="0 0 20 19"><defs><linearGradient id="half"><stop offset="50%" stop-color="#f2c313"/><stop offset="50%" stop-color="#c9c9c9"/></linearGradient></defs><path d="M10 0l3 6.5 7 .8-5.2 4.8 1.4 6.9L10 15.5 3.8 19l1.4-6.9L0 7.3l7-.8z" fill="url(#half)"/></svg>
      <svg width="19" height="18" viewBox="0 0 20 19"><path d="M10 0l3 6.5 7 .8-5.2 4.8 1.4 6.9L10 15.5 3.8 19l1.4-6.9L0 7.3l7-.8z" fill="#c9c9c9"/></svg>
      <svg width="19" height="18" viewBox="0 0 20 19"><path d="M10 0l3 6.5 7 .8-5.2 4.8 1.4 6.9L10 15.5 3.8 19l1.4-6.9L0 7.3l7-.8z" fill="#c9c9c9"/></svg>
    </div>
    <div class="audio">Audio comment<svg width="13" height="13"><circle cx="6.5" cy="6.5" r="6.5" fill="#333"/><path d="M5 3.5 L9.5 6.5 L5 9.5Z" fill="#9bd13b"/></svg></div>
    <p class="excerpt">Elementum ligula, quis congue nunc nisl eu urna.</p>
  </article>

  <article class="video-card" style="left:474px">
    <div class="coach-avatar"></div>
    <div class="coach-name">Commodo Egestas</div>
    <a class="points">need 20 points</a>
    <div class="thumb" role="img" aria-label="Video thumbnail of an infield approach"></div>
    <h3 class="video-title">Nunc blandit, augue vel auctor.</h3>
    <div class="meta"><span class="views">520 188 views</span><br>Difficulty: easy<br>5:13</div>
    <div class="meta right">English<br>USA<br>New York</div>
    <div class="stars">
      <svg width="19" height="18" viewBox="0 0 20 19"><path d="M10 0l3 6.5 7 .8-5.2 4.8 1.4 6.9L10 15.5 3.8 19l1.4-6.9L0 7.3l7-.8z" fill="#f2c313"/></svg>
      <svg width="19" height="18" viewBox="0 0 20 19"><path d="M10 0l3 6.5 7 .8-5.2 4.8 1.4 6.9L10 15.5 3.8 19l1.4-6.9L0 7.3l7-.8z" fill="#f2c313"/></svg>
      <svg width="19" height="18" viewBox="0 0 20 19"><path d="M10 0l3 6.5 7 .8-5.2 4.8 1.4 6.9L10 15.5 3.8 19l1.4-6.9L0 7.3l7-.8z" fill="#f2c313"/></svg>
      <svg width="19" height="18" viewBox="0 0 20 19"><path d="M10 0l3 6.5 7 .8-5.2 4.8 1.4 6.9L10 15.5 3.8 19l1.4-6.9L0 7.3l7-.8z" fill="#c9c9c9"/></svg>
      <svg width="19" height="18" viewBox="0 0 20 19"><path d="M10 0l3 6.5 7 .8-5.2 4.8 1.4 6.9L10 15.5 3.8 19l1.4-6.9L0 7.3l7-.8z" fill="#c9c9c9"/></svg>
    </div>
    <div class="audio">Audio comment<svg width="13" height="13"><circle cx="6.5" cy="6.5" r="6.5" fill="#333"/><path d="M5 3.5 L9.5 6.5 L5 9.5Z" fill="#9bd13b"/></svg></div>
    <p class="excerpt">Elementum ligula, quis congue nunc nisl eu urna. Nam euismod velit aliquam massa venenatis at...</p>
  </article>
</section>

</body>
</html>
```